Home Care App Design

We would like a responsive app design (mobile/web) for an app that will be used by our staff. These need to work display nearly the same for iPhone and Android. The app tracks caregiver tasks (check-in time, daily client activities, caregiver notes, and check out time) and provides updates to team and family members
Updates

I have added individual or grouped pages with better resolution. please let me know if you have any questions

we did not get enough entries so we increase the budget and have not received any new designer entries

Target Market(s)

professional caregivers and family members

Industry/Entity Type

Home Health Care

Font styles to use
Serif

Requirements
Must have
• We currently have a logo - please use colors or slight variants
• We also will need pop-up designs for informational messages and call to actions (with 1-3 options)
Nice to have
• I have attached a sketch of the app, please use this as a guideline. We are looking for ease of use.
• Please feel free to add design aspects that will make it easy to navigate, select options, or enter notes/messages

```html
<!DOCTYPE html>
<html lang="en">
<head>
<meta charset="utf-8">
<title>Homeward – Caregiver App Screens</title>
<link href="https://fonts.googleapis.com/css2?family=Lato:wght@400;700&family=Merriweather:wght@400&display=swap" rel="stylesheet">
<style>
  :root{
    --bg:#d0e4fa;
    --screen:#ffffff;
    --ink:#333a40;
    --muted:#7a7f85;
    --light:#b5b9bd;
    --line:#eeeeee;
    --sky:#1ea7e8;
    --checkin:#4ab8e0;
    --checkout:#ef6b6b;
    --message:#6cc7a8;
    --indigo:#5b63b0;
    --header:#5aa2f5;
    --amber:#fdb827;
    --chart:#3aac1c;
    --tab:#f8f8f8;
    --tab-ink:#b9bcc0;
    --tab-active:#6aaef5;
  }
  *{box-sizing:border-box;margin:0;padding:0}
  html,body{width:1200px;height:1200px;overflow:hidden}
  body{background:var(--bg);font-family:'Lato',sans-serif;color:var(--ink);position:relative}
  .screen{position:absolute;top:347px;width:234px;height:507px;background:var(--screen);
    box-shadow:0 8px 22px rgba(60,90,130,.22);overflow:hidden}
  .screen--login{left:181px}
  .screen--messages{left:483px}
  .screen--team{left:784px}
  .abs{position:absolute}
  .status-time{left:20px;top:8px;font-size:10px;font-weight:700}
  .status-icons{right:10px;top:10px}
  /* login */
  .brand{left:0;width:234px;top:170px;text-align:center;font-family:'Merriweather',serif;font-size:21px;color:#3c5a6b;display:flex;align-items:center;justify-content:center;gap:7px}
  .brand-dot{width:12px;height:12px;border-radius:50%;background:var(--checkin)}
  .field{left:25px;width:184px;height:30px;border:1.5px solid var(--sky);border-radius:15px;font-size:8px;padding-left:15px;display:flex;align-items:center}
  .field--email{top:303px}
  .field--password{top:348px;font-size:10px;letter-spacing:1px}
  .btn-login{left:75px;top:392px;width:84px;height:24px;border-radius:12px;background:var(--sky);color:#fff;font-size:6.5px;font-weight:700;display:flex;align-items:center;justify-content:center}
  /* messages */
  .page-title{left:0;width:234px;top:35px;text-align:center;font-size:12.5px;color:#555}
  .msg{left:9px;width:216px;height:42.5px;border-bottom:1px solid var(--line)}
  .msg-icon{position:absolute;left:12px;top:14px;width:20px;height:20px}
  .msg-date{position:absolute;right:16px;top:2px;font-size:5.5px;color:var(--light)}
  .msg-title{position:absolute;left:39px;top:11px;font-size:11px;font-weight:700;white-space:nowrap}
  .msg-title span{font-size:7.5px;font-weight:400;color:var(--muted);margin-left:3px}
  .msg-sub{position:absolute;left:39px;top:25px;font-size:7.5px;color:var(--muted);white-space:nowrap}
  .avatar-photo{border-radius:50%;background:linear-gradient(135deg,#8a6a55,#3e3230)}
  .fab{left:202px;top:427px;width:20px;height:20px;border-radius:50%;background:#a8ddf5;color:#fff;font-size:16px;line-height:19px;text-align:center}
  .tabbar{left:0;top:457px;width:234px;height:50px;background:var(--tab);border-top:1px solid #ececec}
  /* team */
  .app-header{left:0;top:0;width:234px;height:55px;background:var(--header);color:#fff}
  .app-header .status-time{color:#1d2a38}
  .app-title{left:0;width:234px;top:35px;text-align:center;font-size:12px}
  .sort{right:9px;top:60px;font-size:5px;color:var(--ink);display:flex;align-items:center;gap:4px}
  .sort-select{border:1px solid #999;border-radius:5px;padding:1px 5px;width:34px;display:flex;justify-content:space-between}
  .contact{left:8px;width:218px;border-bottom:1px solid var(--line)}
  .contact-avatar{position:absolute;left:9px;width:44px;height:44px;border-radius:50%}
  .contact-name{position:absolute;left:64px;font-size:10px;font-weight:700}
  .contact-role{position:absolute;left:64px;font-size:7px;color:#555}
  .contact-phone{position:absolute;left:64px;font-size:6px}
  .card{left:6px;top:244px;width:222px;height:207px;border:1px solid #e4e4e4;border-radius:2px;background:#fff}
  .card-head{height:34px;background:var(--amber);color:#fff;font-size:11.5px;font-weight:700;text-align:center;line-height:34px}
  .rating{font-size:8px;color:var(--ink)}
  .badge-label{font-size:6.5px;text-align:center;line-height:7px;width:40px}
  .total-label{left:13px;top:93px;font-size:8px;color:var(--muted)}
  .total-amount{left:13px;top:102px;font-size:16.5px;font-weight:700}
</style>
</head>
<body>

<svg width="0" height="0" style="position:absolute">
  <defs>
    <g id="status">
      <rect x="0" y="4" width="2" height="3" fill="#111"/><rect x="3" y="3" width="2" height="4" fill="#111"/>
      <rect x="6" y="1.5" width="2" height="5.5" fill="#111"/><rect x="9" y="0" width="2" height="7" fill="#111"/>
      <path d="M14 2.5a6 6 0 0 1 8 0M15.5 4.2a3.6 3.6 0 0 1 5 0" stroke="#111" stroke-width="1.1" fill="none"/>
      <circle cx="18" cy="6" r="1" fill="#111"/>
      <rect x="26" y="0.5" width="12" height="6" rx="1.5" fill="#111"/><rect x="38.5" y="2.5" width="1" height="2" fill="#111"/>
    </g>
    <g id="tab-chat"><rect x="1" y="1" width="20" height="15" rx="2"/><path d="M14 16l5 4v-4M5 6h12M5 9.5h12M5 13h8"/></g>
    <g id="tab-people"><circle cx="8" cy="7" r="4"/><path d="M1 20a7 7 0 0 1 14 0"/><circle cx="15" cy="6" r="3.5"/><path d="M16 11a6 6 0 0 1 6 8"/></g>
    <g id="tab-team"><circle cx="11" cy="5" r="3"/><circle cx="4.5" cy="8" r="2.3"/><circle cx="17.5" cy="8" r="2.3"/><path d="M7 21v-8a4 4 0 0 1 8 0v8M1.5 18v-4a3 3 0 0 1 4-2.8M20.5 18v-4a3 3 0 0 0-4-2.8"/></g>
    <g id="tab-clock"><circle cx="13" cy="10" r="8"/><path d="M13 5v5l3 2M2 14l5-2 2 6-5 2z"/></g>
    <g id="tab-tools"><path d="M4 4l6 6M2 6l4-4M12 12l8 8-2 2-8-8M14 3a4 4 0 0 0 5 5l-3 3-5-5z"/></g>
  </defs>
</svg>

<!-- Screen 1: login -->
<section class="screen screen--login">
  <div class="abs status-time">9:41</div>
  <svg class="abs status-icons" width="40" height="8"><use href="#status"/></svg>
  <div class="abs brand"><span class="brand-dot"></span>Homeward</div>
  <div class="abs field field--email">jane.doe@example.com</div>
  <div class="abs field field--password">●●●●●●●</div>
  <div class="abs btn-login">LOGIN</div>
</section>

<!-- Screen 2: messages -->
<section class="screen screen--messages">
  <div class="abs status-time">9:41</div>
  <svg class="abs status-icons" width="40" height="8"><use href="#status"/></svg>
  <h1 class="abs page-title" style="font-weight:400">Messages</h1>

  <div class="abs msg" style="top:58px">
    <svg class="msg-icon" viewBox="0 0 20 20" fill="none" stroke="var(--checkin)" stroke-width="1.4"><path d="M10 19s7-6 7-11A7 7 0 0 0 3 8c0 5 7 11 7 11z"/><circle cx="10" cy="7.5" r="2.2"/><path d="M6.5 12.5a4 4 0 0 1 7 0"/></svg>
    <div class="msg-date">4/1/2019</div>
    <div class="msg-title" style="color:var(--checkin)">Check In<span>@Nora Hale</span></div>
    <div class="msg-sub">14 Elm Road, Brookfield</div>
  </div>
  <div class="abs msg" style="top:100.5px">
    <svg class="msg-icon" viewBox="0 0 20 20" fill="none" stroke="var(--checkout)" stroke-width="1.4"><path d="M10 16s6-5 6-9.5a6 6 0 0 0-12 0C4 11 10 16 10 16z"/><circle cx="10" cy="6.5" r="2"/><path d="M3 19.3h14"/></svg>
    <div class="msg-date">5/1/2019</div>
    <div class="msg-title" style="color:var(--checkout)">Check Out<span>@Nora Hale</span></div>
    <div class="msg-sub">14 Elm Road, Brookfield</div>
  </div>
  <div class="abs msg" style="top:143px">
    <div class="avatar-photo" role="img" aria-label="Sender profile photo" style="position:absolute;left:9px;top:10px;width:25px;height:25px"></div>
    <div class="msg-date">5/1/2019</div>
    <div class="msg-title" style="color:var(--message)">Message<span>@Nora Hale</span></div>
    <div class="msg-sub">Hi! Every thing is fine. All work is done.</div>
  </div>
  <div class="abs msg" style="top:185.5px">
    <svg class="msg-icon" viewBox="0 0 20 20" fill="none" stroke="var(--checkout)" stroke-width="1.4"><path d="M10 16s6-5 6-9.5a6 6 0 0 0-12 0C4 11 10 16 10 16z"/><circle cx="10" cy="6.5" r="2"/><path d="M3 19.3h14"/></svg>
    <div class="msg-date">5/1/2019</div>
    <div class="msg-title" style="color:var(--checkout)">Check Out<span>@Walter</span></div>
    <div class="msg-sub">8 Oak Lane, Riverton</div>
  </div>
  <div class="abs msg" style="top:228px">
    <svg class="msg-icon" viewBox="0 0 20 20" fill="none" stroke="var(--indigo)" stroke-width="1.4"><path d="M5 5h14M5 10h14M5 15h14"/><path d="M1 5h1.5M1 10h1.5M1 15h1.5"/></svg>
    <div class="msg-date">5/1/2019</div>
    <div class="msg-title" style="color:var(--indigo)">Remainders<span>@you</span></div>
    <div class="msg-sub">New appointment</div>
  </div>
  <div class="abs msg" style="top:270.5px">
    <svg class="msg-icon" viewBox="0 0 20 20" fill="none" stroke="var(--indigo)" stroke-width="1.4"><path d="M3 2l4 0 1.5 4-2.3 1.6a11 11 0 0 0 6 6L13.8 11l4 1.5V17a2 2 0 0 1-2 2A15 15 0 0 1 1 4a2 2 0 0 1 2-2z"/></svg>
    <div class="msg-date">5/1/2019</div>
    <div class="msg-title" style="color:var(--indigo)">Call Evan<span>@you</span></div>
    <div class="msg-sub">Remainder</div>
  </div>

  <div class="abs fab">+</div>
  <nav class="abs tabbar">
    <svg width="234" height="50" fill="none" stroke-width="1.4" stroke-linecap="round" stroke-linejoin="round">
      <g transform="translate(15,11)" stroke="var(--tab-active)" stroke-width="2.2"><use href="#tab-chat"/></g>
      <g transform="translate(63,13)" stroke="var(--tab-ink)"><use href="#tab-people"/></g>
      <g transform="translate(109,13)" stroke="var(--tab-ink)"><use href="#tab-team"/></g>
      <g transform="translate(153,13)" stroke="var(--tab-ink)"><use href="#tab-clock"/></g>
      <g transform="translate(200,13)" stroke="var(--tab-ink)"><use href="#tab-tools"/></g>
    </svg>
  </nav>
</section>

<!-- Screen 3: team & earnings -->
<section class="screen screen--team">
  <header class="abs app-header">
    <div class="abs status-time">9:41</div>
    <svg class="abs status-icons" width="40" height="8"><use href="#status"/></svg>
    <div class="abs app-title">Homeward</div>
    <svg class="abs" style="left:210px;top:38px" width="11" height="11" fill="none" stroke="#fff" stroke-width="1.3"><circle cx="5" cy="5" r="3.8"/><path d="M8 8l2.5 2.5"/></svg>
  </header>
  <div class="abs sort">Sort by <span class="sort-select"><span>Name</span><span>▾</span></span></div>

  <div class="abs contact" style="top:66px;height:57px">
    <div class="contact-avatar" role="img" aria-label="Team leader profile photo" style="top:11px;background:linear-gradient(135deg,#8fb0c8,#4d6a80)"></div>
    <div class="contact-name" style="top:16px;font-size:11px">Evan Price</div>
    <div class="contact-role" style="top:29px">Team Leader</div>
    <div class="contact-phone" style="top:42px">Phone: +1 555 010 0199</div>
  </div>
  <div class="abs contact" style="top:123px;height:57px">
    <div class="contact-avatar" role="img" aria-label="Caregiver profile photo" style="top:10px;background:linear-gradient(135deg,#9a7560,#3b2c26)"></div>
    <div class="contact-name" style="top:16px">Mara Quinn</div>
    <div class="contact-role" style="top:27px">Alternate Caregiver</div>
    <div class="contact-phone" style="top:40px">Phone: +1 555 010 0199</div>
  </div>
  <div class="abs contact" style="top:180px;height:56px">
    <div class="contact-avatar" style="top:5px;background:#cfcfcf"></div>
    <div class="contact-name" style="top:15px">Theo Lark</div>
    <div class="contact-role" style="top:26px">Alternate Caregiver</div>
    <div class="contact-phone" style="top:39px">Phone: +1 555 010 0199</div>
  </div>

  <div class="abs card">
    <div class="card-head">Review / Earnings</div>
    <div class="abs rating" style="left:13px;top:47px">Team Rating:</div>
    <div class="abs rating" style="left:16px;top:63px">Your Rating:</div>
    <svg class="abs" style="left:66px;top:46px" width="52" height="30" fill="none" stroke="var(--amber)" stroke-width="0.9">
      <defs><path id="star-sm" d="M5 0.5l1.3 2.8 3 .3-2.3 2 .7 3L5 7.1 2.3 8.6l.7-3-2.3-2 3-.3z"/></defs>
      <use href="#star-sm" x="0"/><use href="#star-sm" x="12.5"/><use href="#star-sm" x="25"/>
      <use href="#star-sm" x="0" y="16"/><use href="#star-sm" x="12.5" y="16"/><use href="#star-sm" x="25" y="16"/><use href="#star-sm" x="37.5" y="16"/>
    </svg>
    <svg class="abs" style="left:129px;top:38px" width="90" height="30" fill="none" stroke="var(--amber)" stroke-width="1">
      <defs><path id="star-lg" d="M15 1l3.8 8.2 9 1-6.7 6 1.9 8.8L15 20.5 7 25l1.9-8.8-6.7-6 9-1z"/></defs>
      <use href="#star-lg"/><use href="#star-lg" x="42"/>
      <text x="15" y="17" font-size="6.5" text-anchor="middle" fill="var(--ink)" stroke="none" font-family="Lato,sans-serif">3.2</text>
      <text x="57" y="17" font-size="6.5" text-anchor="middle" fill="var(--ink)" stroke="none" font-family="Lato,sans-serif">$98.9</text>
    </svg>
    <div class="abs badge-label" style="left:124px;top:70px">Bonus<br>Score</div>
    <div class="abs badge-label" style="left:166px;top:70px">Bonus<br>Amount</div>
    <div class="abs total-label">Total Earnings Amount</div>
    <div class="abs total-amount">$ 4,598.9</div>
    <svg class="abs" style="left:0;top:120px" width="222" height="80" font-family="Lato,sans-serif">
      <g font-size="6" fill="var(--ink)" text-anchor="end">
        <text x="22" y="11">4K</text><text x="22" y="25">3K</text><text x="22" y="38">2K</text><text x="22" y="52">1K</text>
      </g>
      <text x="94" y="12" font-size="6" fill="var(--light)" text-anchor="middle">Earnings by month</text>
      <path d="M27 5V66H166" stroke="#cfd3d6" stroke-width="0.8" fill="none"/>
      <polyline points="32,57 51,41 70,47 100,34 117,40 139,33 159,43" stroke="var(--chart)" stroke-width="1.1" fill="none"/>
      <g font-size="6" fill="var(--ink)" text-anchor="middle">
        <text x="38" y="77">Jan</text><text x="61" y="77">Feb</text><text x="84" y="77">Mar</text>
        <text x="108" y="77">Apr</text><text x="131" y="77">May</text><text x="155" y="77">Jun</text>
      </g>
    </svg>
  </div>

  <nav class="abs tabbar">
    <svg width="234" height="50" fill="none" stroke-width="1.4" stroke-linecap="round" stroke-linejoin="round">
      <g transform="translate(17,14)" stroke="var(--tab-ink)"><use href="#tab-chat"/></g>
      <g transform="translate(61,13)" stroke="var(--tab-ink)"><use href="#tab-people"/></g>
      <g transform="translate(103,6) scale(1.3)" stroke="var(--tab-active)" stroke-width="1.5"><use href="#tab-team"/></g>
      <g transform="translate(154,13)" stroke="var(--tab-ink)"><use href="#tab-clock"/></g>
      <g transform="translate(198,13)" stroke="var(--tab-ink)"><use href="#tab-tools"/></g>
    </svg>
  </nav>
</section>

</body>
</html>
```